FRESH WEB DESIGN FOR A HEALTH - SOCIAL NETWORK

We are currently looking for a creative, fresh, vibrant, inspiring design for a new social network focused on health and nutrition for health professionals (namely nutritionists) and end-users.

Design requirements - IMPORTANT: please see attached file 'LumaGrove web site design scope' for the detailed brief.

The web site requires new design templates with inter-changeable banners and in some cases profile images. It's important for the website to communicate LumaGrove's core values and image which includes fun, vitality, freshness, life fulfillment, trust, integrity and loyalty to the two target groups. Imagery must have a consistent/inter-related theme across all communities, topics and resources, which need to be easily applied to the web site.To help engage our audience we are looking for something fresh and unique in the selected imagery/ theme/ design templates.

The chosen design will need to be applied to create a PDF, PowerPoint and business card template.

Please see attached file 'LumaGrove web site design scope' to view the LumaGrove web site, which is currently under development.

Industry/Entity Type

Nutrition

```html
<!DOCTYPE html>
<html lang="en">
<head>
<meta charset="utf-8">
<title>LumaGrove – The Social Network for Health</title>
<link rel="stylesheet" href="https://fonts.googleapis.com/css2?family=Montserrat:wght@400;600;700&family=Open+Sans:ital,wght@0,400;0,600;1,400&display=swap">
<style>
:root{
  --blue:#1a9ee0;
  --blue-dark:#1589c4;
  --green:#8cc63f;
  --ink:#2b2b2b;
  --muted:#666;
  --grey-band:#efefef;
  --white:#fff;
  --device:#151515;
  --silver:#d9dcdf;
  --silver-dark:#b7bbbf;
  --mini-nav:#3d5a99;
  --mini-line:#e3e6ea;
}
*{margin:0;padding:0;box-sizing:border-box}
html,body{width:1200px;height:3913px;overflow:hidden}
body{position:relative;background:var(--white);font-family:"Open Sans",Arial,sans-serif;color:var(--ink)}
.abs{position:absolute}
.center-text{left:0;width:1200px;text-align:center}

/* header */
.site-header{left:0;top:0;width:1200px;height:89px;background:var(--white);border-top:4px solid var(--blue)}
.brand{left:57px;top:20px;display:flex;align-items:center;gap:10px;font-family:"Montserrat",sans-serif;font-weight:700;font-size:34px;color:var(--green)}
.brand-dot{width:34px;height:34px;border-radius:50%;background:var(--blue)}
.main-nav a{position:absolute;top:47px;font-family:"Montserrat",sans-serif;font-weight:600;font-size:14px;color:var(--ink);text-decoration:none}
.btn{display:flex;align-items:center;justify-content:center;background:var(--blue);color:var(--white);font-family:"Montserrat",sans-serif;font-weight:600;text-decoration:none;border-radius:3px;border-bottom:4px solid var(--blue-dark)}
.btn-nav{left:1054px;top:31px;width:94px;height:39px;font-size:14px}

/* hero */
.hero{left:0;top:89px;width:1200px;height:422px;background:var(--blue)}
.hero-photo{left:78px;top:0;width:287px;height:422px;background:linear-gradient(180deg,#c9a27f 0%,#b98a62 60%,#2a2a2a 92%)}
.hero-title{left:260px;top:82px;width:680px;text-align:center;font-family:"Montserrat",sans-serif;font-weight:700;font-size:50px;line-height:64px;color:var(--white)}
.hero-play{left:548px;top:237px}
.hero-dots{left:570px;top:376px;display:flex;gap:14px}
.hero-dots span{width:11px;height:11px;border-radius:50%;border:2px solid var(--white)}
.hero-dots span.active{background:var(--white)}

/* topics */
.topic{top:613px;width:200px;text-align:center}
.topic-icon{width:136px;height:136px;border-radius:50%;background:var(--blue);margin:0 auto;display:flex;align-items:center;justify-content:center}
.topic-icon.green{background:var(--green)}
.topic-name{margin-top:28px;font-family:"Montserrat",sans-serif;font-weight:600;font-size:15px;color:var(--blue)}
.topic-name.green{color:var(--green)}
.topic-text{margin:8px auto 0;width:160px;font-size:12.5px;line-height:16px;color:var(--muted)}

/* section headings */
.section-title{font-family:"Montserrat",sans-serif;font-weight:700;font-size:33px;color:var(--blue)}
.section-sub{font-size:20px;color:var(--ink)}
.btn-cta{left:490px;top:1114px;width:220px;height:58px;font-size:16px}

/* mini profile page shown on device screens */
.mini{position:absolute;background:var(--white);overflow:hidden;font-family:"Open Sans",sans-serif;color:#333}
.mini-brand{font-family:"Montserrat",sans-serif;font-weight:700;color:var(--green);font-size:2.4em;line-height:1;padding:.35em .5em .3em}
.mini-nav{background:var(--mini-nav);color:var(--white);display:flex;gap:2.2em;font-size:.9em;font-weight:600;padding:.55em 1em;white-space:nowrap}
.mini-profile{display:flex;gap:1.2em;padding:1.2em 1em;border-bottom:1px solid var(--mini-line)}
.mini-avatar{width:6em;height:6em;flex:none;border:1px solid #ccc;background:linear-gradient(180deg,#d9c2ad,#a88669)}
.mini-name{font-size:1.2em;color:#444;padding-top:.4em}
.mini-handle{display:block;width:6em;height:.4em;margin-top:.7em;background:var(--mini-line)}
.mini-tabs{display:flex;gap:1.6em;font-size:.75em;padding:.6em 1em;border-bottom:1px solid var(--mini-line);white-space:nowrap}
.mini-tabs span:first-child{font-weight:600}
.mini-body{display:flex;gap:2em;padding:1em}
.mini-col{flex:1}
.mini-pill{display:inline-block;background:var(--mini-nav);color:#fff;font-size:.7em;padding:.2em .8em;border-radius:1em}
.mini-row{height:.45em;background:var(--mini-line);margin-top:.7em}
.mini-row.short{width:60%}
.mini-box{border:1px solid var(--mini-line);padding:.5em;font-size:.7em}
.mini-count{display:inline-flex;width:2em;height:2em;align-items:center;justify-content:center;background:var(--mini-nav);color:#fff;border-radius:3px;margin-left:1em}

/* tablet preview under CTA */
.device-preview{left:342px;top:1213px;width:514px;height:230px;background:var(--device);border-radius:26px 26px 0 0;overflow:hidden}
.device-preview .mini{left:36px;top:20px;width:442px;height:210px;font-size:10px}
.device-preview .home-btn{right:11px;top:140px;width:12px;height:12px;border-radius:50%;border:1px solid #555}

/* testimonial */
.testimonial{left:0;top:1443px;width:1200px;height:190px;background:var(--grey-band)}
.quote-mark{left:172px;top:42px;font-family:"Montserrat",sans-serif;font-size:56px;color:#444}
.quote-text{left:0;width:1200px;top:58px;text-align:center;font-family:Arial,sans-serif;font-size:21px;color:var(--ink)}
.quote-author{left:0;width:1200px;top:109px;text-align:center;font-family:Arial,sans-serif;font-size:20px;font-style:italic;color:var(--blue)}

/* networks */
.network{width:250px}
.network-photo{width:250px;height:152px}
.network-name{margin-top:26px;font-family:"Montserrat",sans-serif;font-size:19px;color:var(--ink);padding-left:2px}
.btn-signup{left:548px;top:2685px;width:104px;height:50px;font-size:15px}

/* stay connected */
.connected{left:0;top:2812px;width:1200px;height:710px;background:var(--grey-band)}
.laptop-screen{left:884px;top:320px;width:250px;height:164px;background:var(--device);border-radius:12px 12px 0 0}
.laptop-screen .mini{left:12px;top:12px;width:226px;height:152px;font-size:6px}
.laptop-base{left:840px;top:482px;width:302px;height:12px;background:linear-gradient(180deg,var(--silver),var(--silver-dark));border-radius:0 0 14px 14px}
.monitor{left:295px;top:176px;width:592px;height:390px;background:var(--device);border-radius:14px;overflow:hidden}
.monitor .mini{left:16px;top:16px;width:560px;height:316px;font-size:8.5px}
.monitor-chin{left:0;bottom:0;width:592px;height:42px;background:linear-gradient(180deg,var(--silver),var(--silver-dark))}
.monitor-stand{left:520px;top:566px;width:150px;height:88px;background:linear-gradient(180deg,var(--silver-dark),var(--silver));clip-path:polygon(18% 0,82% 0,100% 100%,0 100%)}
.monitor-foot{left:500px;top:650px;width:190px;height:10px;background:var(--silver-dark);border-radius:0 0 6px 6px}
.tablet{left:91px;top:320px;width:274px;height:360px;background:var(--device);border-radius:20px}
.tablet .mini{left:16px;top:26px;width:242px;height:300px;font-size:6.5px}
.phone{left:295px;top:424px;width:123px;height:256px;background:var(--device);border-radius:18px;border:2px solid #444}
.phone .mini{left:7px;top:30px;width:105px;height:188px;font-size:4.5px}
.phone-btn{left:48px;top:226px;width:20px;height:20px;border-radius:50%;border:1px solid #555}

/* footer */
.site-footer{left:0;top:3522px;width:1200px;height:391px;background:var(--blue);color:var(--white)}
.footer-brand{left:57px;top:80px;display:flex;align-items:center;gap:10px;font-family:"Montserrat",sans-serif;font-weight:700;font-size:34px;color:var(--white)}
.footer-brand .brand-dot{background:var(--white)}
.footer-col{top:42px}
.footer-col h4{font-family:"Montserrat",sans-serif;font-weight:400;font-size:21px;margin-bottom:14px}
.footer-col a{display:block;font-size:13px;line-height:29px;color:var(--white);text-decoration:none}
.footer-rule{left:40px;top:303px;width:1120px;height:1px;background:rgba(255,255,255,.45)}
.copyright{left:57px;top:335px;font-size:12px}
.social{left:924px;top:320px;display:flex;gap:8px}
.social span{width:42px;height:42px;border-radius:50%;border:2px solid var(--white)}
.scroll-top{left:1160px;top:334px;font-size:12px}
</style>
</head>
<body>

<header class="site-header abs">
  <div class="brand abs"><span class="brand-dot"></span>LumaGrove</div>
  <nav class="main-nav">
    <a style="left:383px">ABOUT US</a>
    <a style="left:496px">HEALTH NETWORKS</a>
    <a style="left:678px">COMMUNITIES</a>
    <a style="left:824px">RESOURCES</a>
    <a style="left:950px">CONTACT</a>
  </nav>
  <a class="btn btn-nav abs">SIGN UP</a>
</header>

<section class="hero abs">
  <div class="hero-photo abs" role="img" aria-label="Photo of a fit, shirtless man smiling"></div>
  <h1 class="hero-title abs">SHARE YOUR STORY AND<br>SUPPORT OTHERS</h1>
  <svg class="hero-play abs" width="104" height="104" viewBox="0 0 104 104" aria-label="Play video">
    <circle cx="52" cy="52" r="47" fill="none" stroke="#fff" stroke-width="8"/>
    <path d="M40 30 L74 52 L40 74 Z" fill="#fff"/>
  </svg>
  <div class="hero-dots abs"><span></span><span class="active"></span><span></span></div>
</section>

<section class="topics">
  <div class="topic abs" style="left:25px">
    <div class="topic-icon green"><svg width="70" height="70" viewBox="0 0 70 70" fill="none" stroke="#fff" stroke-width="4"><rect x="12" y="20" width="24" height="38" rx="3"/><rect x="15" y="10" width="18" height="10"/><circle cx="48" cy="46" r="12"/></svg></div>
    <div class="topic-name green">NUTRITION</div>
    <p class="topic-text">Sed ut perspiciatis unde omnis iste natus error sit voluptatem</p>
  </div>
  <div class="topic abs" style="left:247px">
    <div class="topic-icon"><svg width="70" height="70" viewBox="0 0 70 70" fill="none" stroke="#fff" stroke-width="5" stroke-linecap="round"><path d="M8 46 q9-8 18 0 t18 0 t18 0"/><path d="M18 34 L40 22 L50 30"/><circle cx="52" cy="18" r="5" fill="#fff"/></svg></div>
    <div class="topic-name">ENERGY</div>
    <p class="topic-text">Sed ut perspiciatis unde omnis iste natus error sit voluptatem</p>
  </div>
  <div class="topic abs" style="left:500px">
    <div class="topic-icon"><svg width="76" height="70" viewBox="0 0 76 70" fill="#fff"><circle cx="26" cy="22" r="10"/><path d="M14 56 h44 a11 11 0 0 0 0-22 a15 15 0 0 0-28-4 a12 12 0 0 0-16 26z"/></svg></div>
    <div class="topic-name">WELLNESS</div>
    <p class="topic-text">Sed ut perspiciatis unde omnis iste natus error sit voluptatem</p>
  </div>
  <div class="topic abs" style="left:743px">
    <div class="topic-icon"><svg width="70" height="70" viewBox="0 0 70 70" fill="none" stroke="#fff" stroke-width="5" stroke-linecap="round"><circle cx="46" cy="14" r="5" fill="#fff"/><path d="M30 22 L42 26 L36 40 L48 50 M36 40 L24 52 M42 26 L52 34"/><path d="M8 30 h12 M12 40 h10 M6 50 h10"/></svg></div>
    <div class="topic-name">EXERCISE</div>
    <p class="topic-text">Sed ut perspiciatis unde omnis iste natus error sit voluptatem</p>
  </div>
  <div class="topic abs" style="left:980px">
    <div class="topic-icon"><svg width="70" height="70" viewBox="0 0 70 70" fill="#fff"><path d="M14 34 a21 20 0 1 1 42 0 c0 8-6 12-8 14 v10 h-14 v-6 h-8 a4 4 0 0 1-4-4 v-6 z"/><circle cx="35" cy="30" r="6" fill="#1a9ee0"/></svg></div>
    <div class="topic-name">MIND</div>
    <p class="topic-text">Sed ut perspiciatis unde omnis iste natus error sit voluptatem</p>
  </div>
</section>

<h2 class="section-title abs center-text" style="top:996px">THE SOCIAL NETWORK FOR HEALTH</h2>
<p class="section-sub abs center-text" style="top:1053px">With over 500 communities to explore, find the right one for your health needs</p>
<a class="btn btn-cta abs">EXPLORE COMMUNITIES</a>

<div class="device-preview abs">
  <div class="mini">
    <div class="mini-brand">LumaGrove</div>
    <div class="mini-nav"><span>My Account</span><span>Groups</span><span>Forums</span><span>Members</span><span>Blog</span><span>FAQ</span><span>Logout</span></div>
    <div class="mini-profile">
      <div class="mini-avatar" role="img" aria-label="Member profile photo"></div>
      <div class="mini-name">Sam Porter<span class="mini-handle"></span></div>
    </div>
  </div>
  <span class="home-btn abs"></span>
</div>

<section class="testimonial abs">
  <span class="quote-mark abs">“</span>
  <p class="quote-text abs">I am being serious when I say I don't know where I would be without WellLinked</p>
  <p class="quote-author abs">Community member, Weight Loss Circle</p>
</section>

<h2 class="section-title abs center-text" style="top:1687px">HEALTH NETWORKS</h2>
<p class="section-sub abs center-text" style="top:1742px">The website consists of 10 health networks as follows:</p>

<section class="networks">
  <div class="network abs" style="left:52px;top:1826px"><div class="network-photo" role="img" aria-label="Photo of a couple cycling outdoors" style="background:linear-gradient(135deg,#7fb35a,#d9c9a8)"></div><div class="network-name">Healthy Lifestyle</div></div>
  <div class="network abs" style="left:331px;top:1826px"><div class="network-photo" role="img" aria-label="Photo of a doctor's desk with a stethoscope" style="background:linear-gradient(135deg,#cfe7f2,#8fbfd8)"></div><div class="network-name">Health Problem</div></div>
  <div class="network abs" style="left:608px;top:1826px"><div class="network-photo" role="img" aria-label="Photo of a woman meditating on grass" style="background:linear-gradient(180deg,#a9c77a,#5f8f3a)"></div><div class="network-name">Weight Loss</div></div>
  <div class="network abs" style="left:895px;top:1826px"><div class="network-photo" role="img" aria-label="Photo of a pregnant woman stretching in a sunny park" style="background:linear-gradient(135deg,#e7d98a,#6f9a3c)"></div><div class="network-name">Pregnancy</div></div>

  <div class="network abs" style="left:52px;top:2082px"><div class="network-photo" role="img" aria-label="Photo of a woman in a sports top" style="background:linear-gradient(135deg,#e8e3dc,#c9a88c)"></div><div class="network-name">Female Health</div></div>
  <div class="network abs" style="left:331px;top:2082px"><div class="network-photo" role="img" aria-label="Photo of a smiling man in a suit" style="background:linear-gradient(135deg,#6b4a36,#2d2420)"></div><div class="network-name">Male Health</div></div>
  <div class="network abs" style="left:608px;top:2082px"><div class="network-photo" role="img" aria-label="Photo of a child eating watermelon" style="background:linear-gradient(135deg,#6fa34a,#d9544a)"></div><div class="network-name">Child Health</div></div>
  <div class="network abs" style="left:895px;top:2082px"><div class="network-photo" role="img" aria-label="Photo of a senior couple jogging" style="background:linear-gradient(180deg,#4f9be0,#8cc36a)"></div><div class="network-name">Senior Health</div></div>

  <div class="network abs" style="left:337px;top:2348px"><div class="network-photo" role="img" aria-label="Photo of a person in a yoga backbend by the sea" style="background:linear-gradient(180deg,#b9d4ea,#e5ddd0)"></div><div class="network-name">Healthy Mind</div></div>
  <div class="network abs" style="left:613px;top:2348px"><div class="network-photo" role="img" aria-label="Photo of a woman running on a forest path" style="background:linear-gradient(180deg,#d7e6c5,#5f8f3a)"></div><div class="network-name">Sports Nutrition</div></div>
</section>

<p class="section-sub abs center-text" style="top:2622px;font-size:19px">Share your experience and follow millions of post from people like you</p>
<a class="btn btn-signup abs">SIGN UP</a>

<section class="connected abs">
  <h2 class="section-title abs center-text" style="top:40px">STAY CONNECTED</h2>
  <p class="section-sub abs center-text" style="top:96px">Designed for everyone. Accessible everywhere</p>

  <div class="laptop-screen abs">
    <div class="mini">
      <div class="mini-nav" style="margin-top:3em"><span>FAQ</span><span>Logout</span></div>
      <div class="mini-profile" style="height:11em"></div>
      <div class="mini-tabs"><span>Groups</span><span>Forums</span><span>Settings</span></div>
      <div class="mini-body"><div class="mini-col"><div class="mini-box">Positive Rating</div><div class="mini-box">Female Points<span class="mini-count">1</span></div></div></div>
    </div>
  </div>
  <div class="laptop-base abs"></div>

  <div class="monitor abs">
    <div class="mini">
      <div class="mini-brand">LumaGrove</div>
      <div class="mini-nav"><span>My Account</span><span>Groups</span><span>Forums</span><span>Members</span><span>Blog</span><span>FAQ</span><span>Logout</span></div>
      <div class="mini-profile">
        <div class="mini-avatar" role="img" aria-label="Member profile photo"></div>
        <div class="mini-name">Sam Porter<span class="mini-handle"></span></div>
      </div>
      <div class="mini-tabs"><span>Dashboard</span><span>Profile</span><span>Notifications</span><span>Messages</span><span>Friends</span><span>Groups</span><span>Forums</span><span>Settings</span></div>
      <div class="mini-body">
        <div class="mini-col"><span class="mini-pill">Dashboard</span><div class="mini-row"></div><div class="mini-row short"></div></div>
        <div class="mini-col"><div class="mini-box">Positive Rating</div><div class="mini-box">Female Points<span class="mini-count">1</span></div><div class="mini-row short"></div></div>
      </div>
    </div>
    <div class="monitor-chin abs"></div>
  </div>
  <div class="monitor-stand abs"></div>
  <div class="monitor-foot abs"></div>

  <div class="tablet abs">
    <div class="mini">
      <div class="mini-brand">LumaGrove</div>
      <div class="mini-nav"><span>My Account</span><span>Groups</span><span>Forums</span></div>
      <div class="mini-profile">
        <div class="mini-avatar" role="img" aria-label="Member profile photo"></div>
        <div class="mini-name">Sam Porter<span class="mini-handle"></span></div>
      </div>
      <div class="mini-tabs"><span>Dashboard</span><span>Profile</span><span>Notifications</span></div>
      <div class="mini-body"><div class="mini-col"><span class="mini-pill">Dashboard</span><div class="mini-row"></div><div class="mini-box" style="margin-top:1em">Female Points</div></div></div>
    </div>
  </div>

  <div class="phone abs">
    <div class="mini">
      <div class="mini-nav" style="margin-top:4em"><span>My Account</span><span>Groups</span></div>
      <div class="mini-profile">
        <div class="mini-avatar" style="width:10em;height:10em" role="img" aria-label="Member profile photo"></div>
      </div>
      <div class="mini-row" style="margin:1em"></div>
      <div class="mini-row short" style="margin:1em"></div>
    </div>
    <span class="phone-btn abs"></span>
  </div>
</section>

<footer class="site-footer abs">
  <div class="footer-brand abs"><span class="brand-dot"></span>LumaGrove</div>
  <div class="footer-col abs" style="left:373px">
    <h4>Company</h4>
    <a>About Us</a><a>Jobs</a><a>Business Model</a><a>Press</a><a>Blog</a>
  </div>
  <div class="footer-col abs" style="left:582px">
    <h4>Communities</h4>
    <a>Directory</a><a>Start a Community</a><a>Community Guidelines</a><a>Community T&amp;C</a>
  </div>
  <div class="footer-col abs" style="left:848px">
    <h4>Support</h4>
    <a>Help Centre</a><a>Users T&amp;C</a><a>Privacy Statement</a><a>Cookies</a>
  </div>
  <div class="footer-col abs" style="left:1044px">
    <h4>Languages</h4>
    <a>English</a><a>Español</a><a>Português</a>
  </div>
  <div class="footer-rule abs"></div>
  <p class="copyright abs">© 2014lumagrove.com. All rights reserved.</p>
  <div class="social abs" aria-label="Social links"><span></span><span></span><span></span><span></span><span></span></div>
  <span class="scroll-top abs">t3</span>
</footer>

</body>
</html>
```